Flyer-Design für EMS-Training
Zielgruppe
EMS-Training
Aufgabenstellung
Meinen bisherigen Flyer habe ich hochgeladen. Der Text kann sich noch etwas ändern. Beibehalten werden sollen die 'Schwünge' und die Farben grün und lila. Diese gehören zum Corporate Design.
Die Bilder, die eingebaut werden sollen, sind ebenfalls hochgeladen.
Gerne hätte ich auf der Seite mit den Adressdaten eine kleine Karte (am besten illustriert), aus der unser Standort erkennbar ist. Um Platz dafür zu schaffen können die Schlagworte 'Gesundheit, Wohlbefinden, Selbstvertrauen' entfallen. Weiterhin entfernt werden kann der QR-Code.
Hintergrund gerne auch dunkel.

```html
<!DOCTYPE html>
<html lang="de">
<head>
<meta charset="utf-8">
<title>Kraftwelle – Flyer EMS-Training</title>
<link href="https://fonts.googleapis.com/css2?family=Montserrat:wght@300;400;600;700;800&display=swap" rel="stylesheet">
<style>
:root{
  --bg:#ececec;
  --paper:#2b2b2b;
  --lime:#c8d400;
  --purple:#7e3a96;
  --white:#ffffff;
  --grey:#b9b9b9;
  --photo-a:#d9d9d9;
  --photo-b:#8f8f8f;
}
*{margin:0;padding:0;box-sizing:border-box}
html,body{width:1200px;height:3053px;overflow:hidden;background:var(--bg);font-family:"Montserrat",sans-serif;color:var(--white)}
.spread{position:absolute;left:45px;width:1110px;height:784px;display:flex;box-shadow:0 20px 50px rgba(0,0,0,.25)}
.spread--outside{top:642px}
.spread--inside{top:1626px}
.panel{position:relative;width:370px;height:784px;background:var(--paper);overflow:hidden;border-right:1px solid #1d1d1d}
.panel:last-child{border-right:none}
.swoosh{position:absolute;left:0;width:100%;pointer-events:none}
.photo{position:absolute;background:linear-gradient(160deg,var(--photo-a),var(--photo-b))}
.heading{font-weight:800;color:var(--lime);font-size:24px;letter-spacing:.5px;line-height:1;white-space:nowrap}
.subheading{font-weight:400;font-size:17px;letter-spacing:.5px;margin-top:3px}
.pulse-line{display:block;margin-top:6px}
.copy{font-size:11.5px;line-height:1.55;color:var(--grey);margin-top:12px}
.icon-circle{flex:none;width:30px;height:30px;border:1.5px solid var(--lime);border-radius:50%}
.benefit{display:flex;gap:14px;margin-top:18px}
.benefit__title{font-weight:700;font-size:12px;text-transform:uppercase;letter-spacing:.3px}
.benefit__text{font-size:10.5px;color:var(--grey);margin-top:3px;line-height:1.4}
.benefit__rule{height:1px;background:var(--lime);margin-top:5px;width:230px}
.cert-box{position:absolute;left:32px;right:32px;bottom:40px;border:2px solid var(--lime);border-radius:18px;padding:18px 16px;text-align:center;font-size:14px;line-height:1.3;font-weight:300}
.cert-box b{font-weight:700}
.brand{display:flex;align-items:center;gap:10px}
.brand__dot{width:34px;height:34px;border-radius:50%;background:var(--purple)}
.brand__name{font-weight:700;font-size:28px;color:var(--lime);letter-spacing:1px}
.contact-row{display:flex;gap:14px;align-items:center;margin-top:20px;font-size:11px;line-height:1.4}
.contact-row .rule{height:1px;background:var(--lime);width:220px;margin-top:4px}
.map{position:absolute;left:40px;right:40px;top:470px;height:190px;border:2px solid var(--lime);border-radius:16px;background:linear-gradient(135deg,#3a3a3a,#2f2f2f)}
.url{position:absolute;left:0;right:0;text-align:center;font-weight:700;font-size:18px}
.badge{position:absolute;width:90px;height:90px;border-radius:50%;background:var(--white);border:3px solid var(--lime)}
.tick-item{display:flex;gap:10px;margin-top:12px;font-size:10.5px;line-height:1.35;color:#e5e5e5}
.tick-item svg{flex:none;margin-top:1px}
.tick-item div{border-bottom:1px solid var(--lime);padding-bottom:6px;width:100%}
.cta-bar{position:absolute;left:150px;right:20px;height:34px;background:var(--lime);color:var(--paper);font-weight:700;display:flex;align-items:center;padding-left:36px}
.cta-icon{position:absolute;left:-18px;top:-2px;width:38px;height:38px;border-radius:50%;background:var(--white);border:3px solid var(--purple);display:flex;align-items:center;justify-content:center}
.feature{display:flex;align-items:center;gap:18px;margin-top:20px}
.feature__icon{flex:none;width:34px;height:34px;border:1.5px solid var(--white);border-radius:8px}
.feature__label{font-weight:700;font-size:13px;text-transform:uppercase;border-bottom:1px solid var(--lime);padding-bottom:4px;width:170px;line-height:1.2}
</style>
</head>
<body>

<section class="spread spread--outside">

  <article class="panel panel--benefits">
    <div style="position:absolute;left:32px;top:50px;right:28px">
      <div class="heading">VORTEILE</div>
      <div class="subheading">BEI KRAFTWELLE</div>
      <svg class="pulse-line" width="300" height="14"><polyline points="0,10 200,10 208,2 214,13 220,10 300,10" fill="none" stroke="var(--lime)" stroke-width="1.2"/></svg>

      <div class="benefit"><div class="icon-circle"></div><div><div class="benefit__title">Persönliche Betreuung</div><div class="benefit__rule"></div><div class="benefit__text">unsere Trainer helfen Ihnen, Ihr persönliches<br>Ziel zu erreichen</div></div></div>
      <div class="benefit"><div class="icon-circle"></div><div><div class="benefit__title">Individuelle Trainingsplanung</div><div class="benefit__rule"></div><div class="benefit__text">für die Erreichung Ihrer persönlichen Trainings-<br>ziele</div></div></div>
      <div class="benefit"><div class="icon-circle"></div><div><div class="benefit__title">Effektives Training</div><div class="benefit__rule"></div><div class="benefit__text">durch Nutzung einer zukunftsweisenden<br>EMS-Technologie</div></div></div>
      <div class="benefit"><div class="icon-circle"></div><div><div class="benefit__title">Hohe Zeitersparnis</div><div class="benefit__rule"></div><div class="benefit__text">20 Minuten pro Woche genügen</div></div></div>
      <div class="benefit"><div class="icon-circle"></div><div><div class="benefit__title">Angenehme Atmosphäre</div><div class="benefit__rule"></div><div class="benefit__text">Man muss es erlebt haben, um es zu spüren</div></div></div>
      <div class="benefit"><div class="icon-circle"></div><div><div class="benefit__title">Ernährungsberatung</div><div class="benefit__rule"></div><div class="benefit__text">von Experten begleitet, um Ihr Trainingsziel<br>zu erreichen</div></div></div>
    </div>
    <div class="cert-box">UNSER TRAININGSGERÄT IST<br><b>MEDIZINISCH ZUGELASSEN</b> UND<br>WURDE IN <b>DEUTSCHLAND</b><br><b>ENTWICKELT &amp; HERGESTELLT</b></div>
  </article>

  <article class="panel panel--contact">
    <div style="position:absolute;left:44px;top:64px">
      <div class="brand"><span class="brand__dot"></span><span class="brand__name">KRAFTWELLE</span></div>
    </div>
    <div style="position:absolute;left:40px;top:160px">
      <div class="contact-row">
        <svg width="26" height="26" viewBox="0 0 26 26"><circle cx="13" cy="13" r="12" fill="none" stroke="var(--white)" stroke-width="1.3"/><circle cx="13" cy="10" r="4" fill="var(--white)"/><path d="M6 20c2-4 12-4 14 0" fill="var(--white)"/></svg>
        <div><b>KRAFTWELLE</b><br>Jonas Lindner<div class="rule"></div></div>
      </div>
      <div class="contact-row">
        <svg width="26" height="26" viewBox="0 0 26 26"><circle cx="13" cy="13" r="12" fill="none" stroke="var(--white)" stroke-width="1.3"/><path d="M13 6a4.5 4.5 0 0 1 4.5 4.5c0 3.5-4.5 8.5-4.5 8.5s-4.5-5-4.5-8.5A4.5 4.5 0 0 1 13 6z" fill="var(--white)"/></svg>
        <div>Am Lindenhof 7<br>38100 Braunschweig<div class="rule"></div></div>
      </div>
      <div class="contact-row">
        <svg width="26" height="26" viewBox="0 0 26 26"><circle cx="13" cy="13" r="12" fill="none" stroke="var(--white)" stroke-width="1.3"/><path d="M9 7l3 3-1.5 2c1 2 2 3 4 4l2-1.5 3 3-2 2c-5 0-10.5-5.5-10.5-10.5z" fill="var(--white)"/></svg>
        <div>Telefonnummer<br>0531 / 48 27 15 30<div class="rule"></div></div>
      </div>
      <div class="contact-row">
        <svg width="26" height="26" viewBox="0 0 26 26"><circle cx="13" cy="13" r="12" fill="none" stroke="var(--white)" stroke-width="1.3"/><rect x="7" y="9" width="12" height="8" fill="none" stroke="var(--white)" stroke-width="1.3"/><polyline points="7,9 13,14 19,9" fill="none" stroke="var(--white)" stroke-width="1.3"/></svg>
        <div>service@kraftwelle.de<br>www.kraftwelle.de<div class="rule"></div></div>
      </div>
    </div>
    <div style="position:absolute;left:0;right:0;top:404px;text-align:center;font-size:17px;line-height:1.1">WIR FREUEN UNS AUF<br><b style="color:var(--lime)">IHREN BESUCH!</b></div>
    <div class="map" role="img" aria-label="Illustrierte Stadtkarte mit markiertem Studiostandort"></div>
    <svg class="swoosh" style="top:690px" height="14"><line x1="40" y1="7" x2="330" y2="7" stroke="var(--lime)" stroke-width="1.2"/></svg>
    <div class="url" style="top:720px">www.kraftwelle.de</div>
  </article>

  <article class="panel panel--cover">
    <div style="position:absolute;left:32px;top:36px">
      <div class="brand"><span class="brand__dot"></span><span class="brand__name">KRAFTWELLE</span></div>
    </div>
    <div class="photo" style="left:0;top:110px;width:370px;height:440px;background:linear-gradient(150deg,#bdbab3,#8a8780)" role="img" aria-label="Foto: Trainerin im EMS-Anzug mit Kettlebell vor einer Betonwand"></div>
    <svg class="swoosh" style="top:95px" width="370" height="80" viewBox="0 0 370 80"><path d="M0 80 C120 10 260 0 370 20 L370 0 L0 0 Z" fill="var(--paper)"/><path d="M0 76 C120 12 260 6 370 26" fill="none" stroke="var(--purple)" stroke-width="12"/></svg>
    <svg class="swoosh" style="top:430px" width="370" height="140" viewBox="0 0 370 140"><path d="M0 140 L0 120 C120 110 260 60 370 0 L370 140 Z" fill="var(--paper)"/><path d="M0 118 C120 108 260 58 370 -2" fill="none" stroke="var(--lime)" stroke-width="14"/><path d="M0 140 C140 128 270 90 370 40" fill="none" stroke="var(--purple)" stroke-width="6"/></svg>
    <div class="badge" style="left:255px;top:385px"></div>
    <div style="position:absolute;left:30px;top:596px">
      <div style="font-weight:800;font-size:40px;color:var(--lime);line-height:1">IN 20 MINUTEN</div>
      <div style="font-weight:700;font-size:22px;margin-top:4px">ZUM TRAININGSERFOLG</div>
    </div>
    <svg class="swoosh" style="top:686px" height="14"><line x1="30" y1="7" x2="340" y2="7" stroke="var(--lime)" stroke-width="1.2"/></svg>
    <div class="url" style="top:714px;font-size:19px">www.kraftwelle.de</div>
  </article>
</section>

<section class="spread spread--inside">

  <article class="panel panel--intro">
    <div style="position:absolute;left:32px;top:50px;right:28px">
      <div class="heading" style="font-size:22px">BEWEGUNG IST WICHTIG</div>
      <div class="subheading" style="font-size:16px">FÜR KÖRPER, GEIST &amp; SEELE</div>
      <svg class="pulse-line" width="310" height="14"><polyline points="0,10 240,10 248,2 254,13 260,10 310,10" fill="none" stroke="var(--lime)" stroke-width="1.2"/></svg>
      <p class="copy">Zu wenig Bewegung lässt unsere Muskeln verkümmern, führt zu Übergewicht und den heute sehr verbreiteten Wohlstandskrankheiten.</p>
      <p class="copy">Rückenschmerzen, Herzkrankheiten, Diabetes oder auch Osteoporose sind nur einige Krankheiten, die durch Bewegungsmangel begünstigt werden.</p>
      <p class="copy">Ein effektives Muskeltraining in Kombination mit der richtigen Ernährung kann diesen Teufelskreis durchbrechen.</p>
      <p class="copy">Sie stärken mit dem Training z.B. die so wichtige Haltemuskulatur im Rücken, erhöhen Ihren täglichen Kalorienverbrauch und steigern Ihre Leistungsfähigkeit im Alltag und im Beruf.</p>
      <p class="copy">Ganz nebenbei profitieren Sie zudem von den nicht zu übersehenden optischen Effekten.</p>
    </div>
    <svg class="swoosh" style="top:470px" width="370" height="120" viewBox="0 0 370 120"><path d="M0 60 C120 20 250 10 370 22" fill="none" stroke="var(--purple)" stroke-width="14"/><path d="M0 100 C120 58 250 48 370 58" fill="none" stroke="var(--purple)" stroke-width="8"/></svg>
    <div class="photo" style="left:0;top:580px;width:370px;height:204px" role="img" aria-label="Foto: Frau im EMS-Anzug bei Bauchübung auf einer Matte"></div>
  </article>

  <article class="panel panel--features">
    <div class="photo" style="left:0;top:0;width:370px;height:250px" role="img" aria-label="Foto: Trainerin im EMS-Anzug mit Kurzhanteln über dem Kopf"></div>
    <svg class="swoosh" style="top:170px" width="370" height="110" viewBox="0 0 370 110"><path d="M0 110 L0 90 C110 40 250 20 370 30 L370 110 Z" fill="var(--paper)"/><path d="M0 92 C110 42 250 22 370 32" fill="none" stroke="var(--lime)" stroke-width="14"/></svg>
    <svg style="position:absolute;left:240px;top:262px" width="80" height="86" viewBox="0 0 80 86"><rect x="34" y="2" width="12" height="7" fill="#fff"/><circle cx="40" cy="48" r="34" fill="none" stroke="#fff" stroke-width="3"/><text x="40" y="44" text-anchor="middle" font-family="Montserrat,sans-serif" font-size="11" fill="#fff">IN NUR</text><text x="40" y="62" text-anchor="middle" font-family="Montserrat,sans-serif" font-size="16" font-weight="800" fill="#c8d400">20MIN</text></svg>
    <div style="position:absolute;left:22px;top:560px;transform:rotate(-90deg);transform-origin:left top;font-weight:700;font-size:12px;white-space:nowrap">IN NUR <span style="color:var(--lime)">20 MINUTEN</span> TRAINING</div>
    <div style="position:absolute;left:80px;top:360px">
      <div class="feature"><div class="feature__icon"></div><div class="feature__label">Starker Rücken,<br>keine Schmerzen</div></div>
      <div class="feature"><div class="feature__icon"></div><div class="feature__label">Trainierte Muskeln</div></div>
      <div class="feature"><div class="feature__icon"></div><div class="feature__label">Weniger Gewicht</div></div>
      <div class="feature"><div class="feature__icon"></div><div class="feature__label">Straffe Haut</div></div>
    </div>
    <div class="photo" style="left:0;top:660px;width:370px;height:124px;background:linear-gradient(160deg,#9a9a9a,#5f5f5f)" role="img" aria-label="Fortsetzung Foto: Beine der Trainierenden auf der Matte"></div>
  </article>

  <article class="panel panel--goals">
    <div style="position:absolute;left:30px;top:50px;right:26px">
      <div class="heading">TRAININGSZIELE</div>
      <div class="subheading">BEI KRAFTWELLE</div>
      <svg class="pulse-line" width="310" height="14"><polyline points="0,10 250,10 258,2 264,13 270,10 310,10" fill="none" stroke="var(--lime)" stroke-width="1.2"/></svg>
      <div class="tick-item"><svg width="14" height="14"><circle cx="7" cy="7" r="6" fill="none" stroke="#c8d400"/><polyline points="4,7 6,9.5 10,4.5" fill="none" stroke="#c8d400" stroke-width="1.5"/></svg><div>Aufbau und Erhalt der Muskulatur</div></div>
      <div class="tick-item"><svg width="14" height="14"><circle cx="7" cy="7" r="6" fill="none" stroke="#c8d400"/><polyline points="4,7 6,9.5 10,4.5" fill="none" stroke="#c8d400" stroke-width="1.5"/></svg><div>Stabilisierung des Halteapparates durch Kräftigung der Haltemuskeln</div></div>
      <div class="tick-item"><svg width="14" height="14"><circle cx="7" cy="7" r="6" fill="none" stroke="#c8d400"/><polyline points="4,7 6,9.5 10,4.5" fill="none" stroke="#c8d400" stroke-width="1.5"/></svg><div>Kräftigung der tiefen Muskelschichten, die herkömmliches Training nur schwer erreicht</div></div>
      <div class="tick-item"><svg width="14" height="14"><circle cx="7" cy="7" r="6" fill="none" stroke="#c8d400"/><polyline points="4,7 6,9.5 10,4.5" fill="none" stroke="#c8d400" stroke-width="1.5"/></svg><div>Linderung von Rücken- und Gelenkproblemen</div></div>
      <div class="tick-item"><svg width="14" height="14"><circle cx="7" cy="7" r="6" fill="none" stroke="#c8d400"/><polyline points="4,7 6,9.5 10,4.5" fill="none" stroke="#c8d400" stroke-width="1.5"/></svg><div>Training der Ausdauer und des Herz-Kreislauf-Systems</div></div>
      <div class="tick-item"><svg width="14" height="14"><circle cx="7" cy="7" r="6" fill="none" stroke="#c8d400"/><polyline points="4,7 6,9.5 10,4.5" fill="none" stroke="#c8d400" stroke-width="1.5"/></svg><div>Stoffwechsel-Training – Anregen der Fettverbrennung und Gewichtsreduktion</div></div>
      <div class="tick-item"><svg width="14" height="14"><circle cx="7" cy="7" r="6" fill="none" stroke="#c8d400"/><polyline points="4,7 6,9.5 10,4.5" fill="none" stroke="#c8d400" stroke-width="1.5"/></svg><div>Straffung der Haut und damit verbunden der Abbau von Cellulite</div></div>
    </div>
    <div class="photo" style="left:0;top:520px;width:120px;height:264px;background:linear-gradient(160deg,#8d8d8d,#4a4a4a)" role="img" aria-label="Foto: Trainerin in der Kniebeuge mit Kettlebell"></div>
    <svg class="swoosh" style="top:520px" height="14"><polyline points="150,10 250,10 256,2 262,13 268,10 350,10" fill="none" stroke="var(--lime)" stroke-width="1.2"/></svg>
    <div style="position:absolute;left:140px;right:16px;top:542px;text-align:center;font-size:12px;line-height:1.4">Legen Sie noch heute den Grundstein für eine gesunde Zukunft. Vereinbaren Sie jetzt Ihr kostenloses<div style="font-weight:800;font-size:20px;margin-top:4px">PROBETRAINING!</div></div>
    <div class="cta-bar" style="top:652px;font-size:15px"><span class="cta-icon"><svg width="16" height="16" viewBox="0 0 26 26"><path d="M6 3l5 5-2.5 3c1.5 3 3.5 5 6.5 6.5l3-2.5 5 5-3 3C12 23 3 14 3 6z" fill="var(--purple)"/></svg></span>0531 / 48 27 15 30</div>
    <div class="cta-bar" style="top:710px;font-size:12px;font-weight:400"><span class="cta-icon"><svg width="18" height="18" viewBox="0 0 20 20"><circle cx="10" cy="10" r="8" fill="none" stroke="var(--purple)" stroke-width="1.6"/><ellipse cx="10" cy="10" rx="3.5" ry="8" fill="none" stroke="var(--purple)" stroke-width="1.3"/><line x1="2" y1="10" x2="18" y2="10" stroke="var(--purple)" stroke-width="1.3"/></svg></span>www.kraftwelle.de</div>
  </article>
</section>

</body>
</html>
```